New Business Card for Auto Repair and Performance Shop!

Need a redesign on a card that we have used for a while now. Something more update and modern, Serious but not too serious. Something confident, that shows the client that we are bespoke. Adding value.

Target Market(s)

Foreign Auto Repair and Performance

Industry/Entity Type

Automotive

Contact Information for Business Card

Utilize Logo, would like to change car silhouette to something Verso,

Font styles to use
Sans Serif

Requirements
Must have
• business name, address, website, phone number.
MotoRadiance
5182 W. Birchfold Rd
Brenmoor, T.X. 70913
1-555-468-3172
www.moto-radence.example

Specializing in Asian, European, and Domestic Auto Repair, Performance and Fabrication.

Clear space on back to for space to write appointment time and which client advisor helped the client.
Nice to have
• Up to the designers,

```html
<!DOCTYPE html>
<html lang="en">
<head>
<meta charset="utf-8">
<title>MotoRadiance Business Card</title>
<link href="https://fonts.googleapis.com/css2?family=Lato:wght@300;400;700&display=swap" rel="stylesheet">
<style>
  :root {
    --stage: #3a3633;
    --card: #1f1f1f;
    --card-edge: #141414;
    --band-dark: #171717;
    --band-light: #2b2b2b;
    --ink: #f2f2f2;
    --ink-soft: #d9d9d9;
    --ink-faint: #2c2c2c;
    --accent: #b3262b;
    --field: #ffffff;
  }
  * { margin: 0; padding: 0; box-sizing: border-box; }
  html, body { width: 1200px; height: 900px; overflow: hidden; }
  body {
    background: var(--stage);
    font-family: "Lato", sans-serif;
    color: var(--ink);
    position: relative;
  }
  .card {
    position: absolute;
    top: 100px;
    width: 400px;
    height: 700px;
    background: var(--card);
    border-radius: 44px;
    box-shadow: 0 0 0 1px var(--card-edge);
    overflow: hidden;
  }
  .card--front { left: 150px; }
  .card--back { left: 650px; }

  .fold-band {
    position: absolute;
    left: 0; width: 100%;
    height: 90px;
  }
  .card--front .fold-band { top: 290px; }
  .card--back .fold-band { top: 150px; }

  .brand {
    position: absolute;
    left: 0; width: 100%;
    display: flex;
    align-items: center;
    justify-content: center;
    gap: 14px;
    font-weight: 700;
    letter-spacing: 1px;
  }
  .brand-dot {
    width: 18px; height: 18px;
    border-radius: 50%;
    background: var(--accent);
  }
  .card--front .brand { top: 95px; font-size: 38px; color: var(--ink); }
  .card--back .brand { top: 70px; font-size: 38px; color: var(--ink-faint); }
  .card--back .brand-dot { background: var(--ink-faint); }

  .specialty {
    position: absolute;
    top: 190px; left: 40px; right: 40px;
    text-align: center;
    font-size: 17px;
    line-height: 1.35;
    text-transform: uppercase;
    letter-spacing: 0.5px;
    color: var(--ink-soft);
  }

  .field-label {
    position: absolute;
    left: 0; width: 100%;
    text-align: center;
    font-size: 22px;
    color: var(--ink);
  }
  .field-box {
    position: absolute;
    left: 42px; right: 42px;
    height: 68px;
    background: var(--field);
    border-radius: 14px;
  }
  .label-appointment { top: 400px; }
  .box-appointment { top: 440px; }
  .label-advisor { top: 540px; }
  .box-advisor { top: 580px; }

  .contact-frame {
    position: absolute;
    top: 230px; left: 40px; right: 40px;
    height: 270px;
    border: 1.5px solid var(--ink-soft);
  }
  .contact-icons {
    position: absolute;
    top: -14px; left: 50%;
    transform: translateX(-50%);
    background: var(--card);
    padding: 0 12px;
    display: flex;
    gap: 20px;
  }
  .contact-list {
    position: absolute;
    top: 50px; left: 0; width: 100%;
    list-style: none;
    text-align: center;
    font-size: 22px;
    line-height: 2.1;
  }
  .address-frame {
    position: absolute;
    top: 555px; left: 40px; right: 40px;
    height: 80px;
    border: 1.5px solid var(--ink-soft);
    display: flex;
    align-items: center;
    justify-content: center;
    text-align: center;
    font-size: 16px;
    line-height: 1.3;
  }
  .address-icon {
    position: absolute;
    top: -14px; left: 50%;
    transform: translateX(-50%);
    background: var(--card);
    padding: 0 10px;
  }
</style>
</head>
<body>

<section class="card card--front">
  <div class="brand"><span class="brand-dot"></span>MotoRadiance</div>
  <p class="specialty">Specializing in Asian, European, and Domestic Auto Repair, Performance and Fabrication.</p>
  <svg class="fold-band" viewBox="0 0 400 90" preserveAspectRatio="none">
    <defs>
      <linearGradient id="bandFront" x1="0" y1="0" x2="0" y2="1">
        <stop offset="0" stop-color="var(--band-light)"/>
        <stop offset="1" stop-color="var(--band-dark)"/>
      </linearGradient>
    </defs>
    <path d="M0 0 L200 45 L400 0 L400 45 L200 90 L0 45 Z" fill="url(#bandFront)"/>
  </svg>
  <p class="field-label label-appointment">Appointment time</p>
  <div class="field-box box-appointment"></div>
  <p class="field-label label-advisor">Client-advisor</p>
  <div class="field-box box-advisor"></div>
</section>

<section class="card card--back">
  <div class="brand"><span class="brand-dot"></span>MotoRadiance</div>
  <svg class="fold-band" viewBox="0 0 400 90" preserveAspectRatio="none">
    <defs>
      <linearGradient id="bandBack" x1="0" y1="0" x2="0" y2="1">
        <stop offset="0" stop-color="var(--band-light)"/>
        <stop offset="1" stop-color="var(--band-dark)"/>
      </linearGradient>
    </defs>
    <path d="M0 0 L200 45 L400 0 L400 45 L200 90 L0 45 Z" fill="url(#bandBack)"/>
  </svg>

  <div class="contact-frame">
    <div class="contact-icons">
      <svg width="24" height="24" viewBox="0 0 24 24" aria-label="Phone"><path d="M3 9 Q12 2 21 9 L18 12 L15 10 L9 10 L6 12 Z M6 13 H18 V20 H6 Z" fill="var(--ink)"/><circle cx="12" cy="16.5" r="2" fill="var(--card)"/></svg>
      <svg width="24" height="24" viewBox="0 0 24 24" aria-label="Email"><path d="M2 11 L22 3 L15 21 L11 13 Z" fill="var(--ink)"/></svg>
      <svg width="24" height="24" viewBox="0 0 24 24" aria-label="Website"><g fill="none" stroke="var(--ink)" stroke-width="1.3"><circle cx="12" cy="12" r="9"/><ellipse cx="12" cy="12" rx="4" ry="9"/><line x1="3" y1="12" x2="21" y2="12"/><line x1="5" y1="7" x2="19" y2="7"/><line x1="5" y1="17" x2="19" y2="17"/></g></svg>
    </div>
    <ul class="contact-list">
      <li>1-555-468-3172</li>
      <li>info@moto-radence.example</li>
      <li>www.moto-radence.example</li>
    </ul>
  </div>

  <div class="address-frame">
    <svg class="address-icon" width="40" height="24" viewBox="0 0 24 24" aria-label="Address"><path d="M12 3 L22 12 H19 V21 H14 V15 H10 V21 H5 V12 H2 Z" fill="var(--ink)"/></svg>
    <p>5182 W. Birchfold Rd<br>Brenmoor, T.X. 70913</p>
  </div>
</section>

</body>
</html>
```